Design a For Sale sign board and Direction Sign Board.
Attached is an example of what i am thinking but am happy to look at any options.
Colours are to be ""bright Orange"on white and in reverse as well.

Logo id Fairbrook & Co Real Estate.

```html
<!DOCTYPE html>
<html lang="en">
<head>
<meta charset="utf-8">
<title>Fairbrook &amp; Co Real Estate – Sign Boards</title>
<link rel="stylesheet" href="https://fonts.googleapis.com/css2?family=Poppins:wght@300;500;600&display=swap">
<style>
  :root {
    --orange: #f9a51e;
    --white: #ffffff;
  }
  * { margin: 0; padding: 0; box-sizing: border-box; }
  html, body {
    width: 1200px;
    height: 848px;
    overflow: hidden;
    font-family: "Poppins", sans-serif;
  }
  .sheet {
    position: relative;
    width: 1200px;
    height: 848px;
  }
  .band {
    position: absolute;
    left: 0;
    width: 1200px;
    height: 424px;
  }
  .band--light { top: 0; background: var(--white); color: var(--orange); }
  .band--dark { top: 424px; background: var(--orange); color: var(--white); }

  .sign {
    position: absolute;
    top: 128px;
    width: 420px;
    display: flex;
    flex-direction: column;
    align-items: center;
    text-align: center;
  }
  .sign--direction { left: 127px; }
  .sign--sale { left: 653px; }

  .brand {
    display: flex;
    flex-direction: column;
    align-items: center;
    font-weight: 500;
    line-height: 1;
  }
  .brand__name {
    font-size: 46px;
    letter-spacing: 0.02em;
  }
  .brand__sub {
    margin-top: 14px;
    font-size: 21px;
    letter-spacing: 0.42em;
    margin-right: -0.42em;
  }

  .agent {
    margin-top: 26px;
    font-size: 35px;
    font-weight: 600;
    letter-spacing: 0.3em;
    margin-right: -0.3em;
    line-height: 1;
  }
  .phone {
    margin-top: 10px;
    font-size: 25px;
    font-weight: 300;
    letter-spacing: 0.28em;
    margin-right: -0.28em;
    line-height: 1;
  }
  .arrow {
    margin-top: 12px;
    width: 116px;
    height: 22px;
    display: block;
  }
  .arrow path { fill: currentColor; }
</style>
</head>
<body>
<main class="sheet">
  <section class="band band--light">
    <div class="sign sign--direction">
      <div class="brand">
        <span class="brand__name">Fairbrook &amp; Co</span>
        <span class="brand__sub">Real Estate</span>
      </div>
      <p class="agent">Daniel Hart</p>
      <svg class="arrow" viewBox="0 0 116 22" aria-label="Arrow pointing left" role="img">
        <path d="M0 11 L18 0 V8.5 H116 V13.5 H18 V22 Z"/>
      </svg>
    </div>
    <div class="sign sign--sale">
      <div class="brand">
        <span class="brand__name">Fairbrook &amp; Co</span>
        <span class="brand__sub">Real Estate</span>
      </div>
      <p class="agent">Daniel Hart</p>
      <p class="phone">0412 555 018</p>
    </div>
  </section>

  <section class="band band--dark">
    <div class="sign sign--direction">
      <div class="brand">
        <span class="brand__name">Fairbrook &amp; Co</span>
        <span class="brand__sub">Real Estate</span>
      </div>
      <p class="agent">Daniel Hart</p>
      <svg class="arrow" viewBox="0 0 116 22" aria-label="Arrow pointing left" role="img">
        <path d="M0 11 L18 0 V8.5 H116 V13.5 H18 V22 Z"/>
      </svg>
    </div>
    <div class="sign sign--sale">
      <div class="brand">
        <span class="brand__name">Fairbrook &amp; Co</span>
        <span class="brand__sub">Real Estate</span>
      </div>
      <p class="agent">Daniel Hart</p>
      <p class="phone">0412 555 018</p>
    </div>
  </section>
</main>
</body>
</html>
```